New Business Card for Software Company

We are looking at rebranding a 10 year old company that specializes in PDF and DWF solutions for Architects and Engineers. We will attach the new company logo that we are going with so you can work with that and complimentary colors.
The sample information we would like on the business card is:
Gerald Pembrook
Vice President
4173 W. Tillman Avenue. STE 306
PMB#417
Mesa, AZ 85316
866-392-7154 US Toll Free
123-581-3064 Cell
gpembrook@vextrolan.com
The old tag line that we had on the business cars was.
Providing Industrial Strength PDF and DWF Solutions to the Global CAD Marketplace.
If you have an idea for a better tag line we are open to that also.
Updates
We would like to thank all of the Designers for their wonderful work. We apologize that we will not have the time to provide feedback to everyone. There is just so many innovative and professional designs that you have all created making our decision even harder.
Target Market(s)
Architects and Engineers
Industry/Entity Type
Business
Look and feel
Each slider illustrates characteristics of the customer's brand and the style your logo design should communicate.

```html
<!DOCTYPE html>
<html lang="en">
<head>
<meta charset="utf-8">
<title>Vextrolan Business Card</title>
<link href="https://fonts.googleapis.com/css2?family=Fira+Sans:ital,wght@0,400;1,400;1,600&family=Montserrat:ital,wght@0,400;0,700;1,400&display=swap" rel="stylesheet">
<style>
  :root {
    --page-bg: #1e1e1e;
    --card-bg: #f4f4f4;
    --accent: #e8611f;
    --ink: #3a3a3a;
    --ink-strong: #222222;
    --ink-soft: #6e6e6e;
    --photo-light: #fbfbfb;
    --photo-mid: #e6e6e6;
    --photo-dark: #d2d2d2;
  }
  * { margin: 0; padding: 0; box-sizing: border-box; }
  html, body {
    width: 1200px;
    height: 1200px;
    overflow: hidden;
    background: var(--page-bg);
  }
  .canvas {
    position: relative;
    width: 1200px;
    height: 1200px;
  }
  .business-card {
    position: absolute;
    left: 100px;
    top: 314px;
    width: 1000px;
    height: 572px;
    background: var(--card-bg);
    overflow: hidden;
  }
  .blueprint-photo {
    position: absolute;
    inset: 0;
    background:
      radial-gradient(circle at 32% 30%, var(--photo-light) 0 12%, transparent 30%),
      radial-gradient(circle at 62% 22%, var(--photo-light) 0 10%, transparent 26%),
      radial-gradient(circle at 12% 75%, var(--photo-light) 0 10%, transparent 28%),
      linear-gradient(160deg, var(--photo-mid) 0%, var(--photo-light) 45%, var(--photo-dark) 100%);
  }
  .contact-block {
    position: absolute;
    left: 62px;
    top: 56px;
    padding-left: 34px;
    border-left: 7px solid var(--accent);
    font-family: "Fira Sans", sans-serif;
    font-size: 24px;
    line-height: 1.3;
    color: var(--ink);
  }
  .contact-block .address { margin-bottom: 18px; }
  .identity {
    position: absolute;
    left: 640px;
    top: 270px;
  }
  .brand {
    display: flex;
    align-items: center;
    gap: 12px;
    font-family: "Montserrat", sans-serif;
    font-weight: 700;
    font-size: 38px;
    color: var(--accent);
    margin-bottom: 14px;
  }
  .brand-dot {
    width: 36px;
    height: 36px;
    border-radius: 50%;
    background: var(--accent);
  }
  .person-name {
    font-family: "Montserrat", sans-serif;
    font-weight: 700;
    font-size: 34px;
    color: var(--ink-strong);
    line-height: 1.1;
  }
  .person-title {
    font-family: "Montserrat", sans-serif;
    font-style: italic;
    font-size: 25px;
    color: var(--ink);
    margin-top: 4px;
  }
  .tagline {
    position: absolute;
    left: 40px;
    right: 40px;
    bottom: 50px;
    text-align: center;
    font-family: "Fira Sans", sans-serif;
    font-style: italic;
    font-weight: 600;
    font-size: 22px;
    color: var(--ink-soft);
  }
</style>
</head>
<body>
<main class="canvas">
  <section class="business-card">
    <div class="blueprint-photo" role="img" aria-label="Photograph of rolled architectural blueprints and technical drawings in soft grey tones"></div>

    <div class="contact-block">
      <p class="address">4173 W. Tillman Avenue. STE 306<br>PMB#417 Mesa, AZ 85316</p>
      <p class="phones">866-392-7154 US Toll Free<br>123-581-3064 Cell<br>gpembrook@vextrolan.com</p>
    </div>

    <div class="identity">
      <div class="brand"><span class="brand-dot"></span><span class="brand-name">Vextrolan</span></div>
      <h1 class="person-name">Gerald Pembrook</h1>
      <p class="person-title">Vice President</p>
    </div>

    <p class="tagline">Providing Industrial Strength PDF and DWF Solutions to the Global CAD Marketplace.</p>
  </section>
</main>
</body>
</html>
```